Book Cover Design Project

We need a book cover for a eBook on internet banking.

This eBook is meant to be an easy to read, practical book to help people understand what internet banking is, the pros and cons and cover the pure 'internet only' banks that have no branches. The intention is to help people to make informed decisions about whether to use internet banking, how to use it safely and explain in detail what 'internet only' banks are and whether they are right for them.

The cover should not look technical so that non-technical people are not scared off by the look. I have uploaded a book cover design that has the style that I am trying to portray, I have also uploaded a front cover that I created but do not think is suitable.

The cover wording layout could be something like
"Internet Banking"
"A practical guide to answer all your questions" or "The ultimate guide to internet banking" or "The Who's What's and How's of Internet Banking"
Authors name : Colin Pettifer

Industry/Entity Type

Internet

```html
<!DOCTYPE html>
<html lang="en">
<head>
<meta charset="utf-8">
<title>The Who's, What's and How's of Internet Banking</title>
<link href="https://fonts.googleapis.com/css2?family=PT+Sans:wght@400;700&family=Cinzel:wght@400;600&display=swap" rel="stylesheet">
<style>
  :root {
    --sky-top: #3f86c9;
    --sky-mid: #a9cdee;
    --sky-light: #e6f1fb;
    --white: #ffffff;
    --banner: #f4eedb;
    --banner-edge: #e4dbbf;
    --ink: #1e2b45;
    --ink-soft: #33405a;
    --wave-deep: #1665b8;
    --wave-mid: #2f86d6;
    --wave-light: #7ab8ea;
    --silver: #c9ced4;
    --cash: #a9b893;
  }
  html, body {
    margin: 0;
    padding: 0;
    overflow: hidden;
  }
  .cover {
    position: relative;
    width: 800px;
    height: 1200px;
    overflow: hidden;
    background: linear-gradient(180deg, var(--sky-top) 0%, var(--sky-mid) 22%, var(--sky-light) 45%, var(--white) 60%, var(--white) 100%);
  }
  .cover-backdrop {
    position: absolute;
    inset: 0;
    width: 800px;
    height: 1200px;
  }
  .cover-art {
    position: absolute;
    left: 265px;
    top: 80px;
    width: 380px;
    height: 500px;
    border-radius: 18px;
    background:
      radial-gradient(ellipse at 50% 75%, var(--cash) 0%, rgba(169,184,147,0.6) 40%, rgba(169,184,147,0) 70%),
      linear-gradient(160deg, #3a3f45 0%, #6f757c 35%, var(--silver) 60%, rgba(255,255,255,0) 100%);
    opacity: 0.9;
  }
  .title-banner {
    position: absolute;
    left: 0;
    top: 688px;
    width: 800px;
    height: 166px;
    background: linear-gradient(90deg, var(--banner-edge) 0%, var(--banner) 12%, var(--banner) 100%);
    box-shadow: 0 4px 10px rgba(30, 43, 69, 0.18);
    display: flex;
    flex-direction: column;
    justify-content: center;
    align-items: center;
  }
  .title {
    margin: 0;
    font-family: "PT Sans", sans-serif;
    font-weight: 400;
    font-size: 50px;
    line-height: 1.22;
    color: var(--ink-soft);
    text-align: center;
    letter-spacing: 0.2px;
  }
  .title strong {
    font-weight: 700;
    color: var(--ink);
  }
  .author {
    position: absolute;
    left: 0;
    bottom: 22px;
    width: 800px;
    margin: 0;
    text-align: center;
    font-family: "Cinzel", serif;
    font-weight: 400;
    font-size: 52px;
    letter-spacing: 5px;
    color: var(--white);
    text-shadow: 0 1px 3px rgba(22, 101, 184, 0.45);
  }
</style>
</head>
<body>
  <main class="cover">
    <svg class="cover-backdrop" viewBox="0 0 800 1200" aria-hidden="true">
      <defs>
        <linearGradient id="wave-band" x1="0" y1="0" x2="0" y2="1">
          <stop offset="0" stop-color="var(--wave-light)"/>
          <stop offset="0.45" stop-color="var(--wave-deep)"/>
          <stop offset="1" stop-color="var(--wave-mid)"/>
        </linearGradient>
        <linearGradient id="foot-band" x1="0" y1="0" x2="0" y2="1">
          <stop offset="0" stop-color="#a9d3f4"/>
          <stop offset="1" stop-color="#5fa6e2"/>
        </linearGradient>
      </defs>
      <!-- sky swooshes -->
      <path d="M -40 260 C 180 120, 480 70, 860 150" fill="none" stroke="var(--white)" stroke-width="6" opacity="0.75"/>
      <path d="M -40 320 C 220 180, 520 150, 860 230" fill="none" stroke="var(--white)" stroke-width="3" opacity="0.6"/>
      <path d="M -40 200 C 200 90, 520 40, 860 90" fill="none" stroke="var(--white)" stroke-width="2" opacity="0.5"/>
      <path d="M -40 420 C 260 300, 560 300, 860 360" fill="none" stroke="var(--white)" stroke-width="4" opacity="0.55"/>
      <!-- lower wave band -->
      <path d="M 0 930 C 200 880, 520 960, 800 900 L 800 1200 L 0 1200 Z" fill="url(#wave-band)"/>
      <path d="M 0 955 C 230 905, 520 990, 800 925" fill="none" stroke="var(--white)" stroke-width="4" opacity="0.7"/>
      <path d="M 0 985 C 260 935, 540 1015, 800 955" fill="none" stroke="var(--white)" stroke-width="2" opacity="0.5"/>
      <path d="M 0 1080 C 240 1040, 540 1110, 800 1060 L 800 1200 L 0 1200 Z" fill="url(#foot-band)"/>
      <path d="M 0 1080 C 240 1040, 540 1110, 800 1060" fill="none" stroke="var(--white)" stroke-width="5" opacity="0.85"/>
    </svg>

    <div class="cover-art" role="img" aria-label="Open silver briefcase overflowing with stacks of banknotes"></div>

    <header class="title-banner">
      <h1 class="title">The <strong>Who's</strong>, <strong>What's</strong> and<br><strong>How's</strong> of <strong>Internet Banking</strong></h1>
    </header>

    <p class="author">Colin Pettifer</p>
  </main>
</body>
</html>
```